business cards for Tramvex
Tramvexa
business cards for Tramvex - Government
Modern
R.K.Dunmore
914 E Harlan Avenue, Suite 215 Fort Worth, TX 76102
rdunmore@tramvexa-mail.com
www.tramvexa-site.com
need to be able to create cards for other people- the backside is logo only- the front needs my name then tramvexa with address email phone number and website- please put logo on front side as well. colors can be red/white/blue/ black or any combination
big version of logo and possibly ability to write on it- this may not work out well so if it doesn't then don't do it.

```html
<!DOCTYPE html>
<html lang="en">
<head>
<meta charset="utf-8">
<title>Tramvexa business cards</title>
<link rel="stylesheet" href="https://fonts.googleapis.com/css2?family=Cinzel:wght@600&family=Open+Sans:wght@400;600;700&display=swap">
<style>
  :root {
    --navy: #2d4266;
    --red: #9b2430;
    --white: #ffffff;
    --stage: #e9eaec;
    --ink: #2d4266;
  }
  html, body {
    margin: 0;
    padding: 0;
    width: 1200px;
    height: 902px;
    overflow: hidden;
    background: var(--stage);
    font-family: "Open Sans", Arial, sans-serif;
  }
  .sheet {
    position: relative;
    width: 1200px;
    height: 902px;
  }
  .card {
    position: absolute;
    left: 270px;
    width: 660px;
    height: 377px;
    background: var(--white);
    box-shadow: 0 4px 14px rgba(0,0,0,0.12);
    overflow: hidden;
  }
  .card--back { top: 52px; }
  .card--front { top: 473px; }

  .brand {
    display: flex;
    align-items: center;
    gap: 12px;
    color: var(--ink);
    font-family: "Cinzel", Georgia, serif;
    font-weight: 600;
    white-space: nowrap;
  }
  .brand__mark {
    background: var(--navy);
    flex: none;
  }
  .card--back .brand {
    position: absolute;
    left: 50%;
    top: 50%;
    transform: translate(-50%, -50%);
    font-size: 44px;
  }
  .card--back .brand__mark { width: 40px; height: 40px; }

  .card--front .brand {
    position: absolute;
    left: 34px;
    top: 104px;
    font-size: 30px;
    gap: 10px;
  }
  .card--front .brand__mark { width: 28px; height: 28px; }

  .swoosh {
    position: absolute;
    inset: 0;
    width: 660px;
    height: 377px;
  }

  .holder {
    position: absolute;
    left: 34px;
    top: 236px;
    color: var(--ink);
  }
  .holder__name {
    font-weight: 700;
    font-size: 17px;
    margin: 0;
  }
  .holder__role {
    font-size: 15px;
    margin: 2px 0 0;
  }

  .contact {
    position: absolute;
    right: 26px;
    top: 100px;
    list-style: none;
    margin: 0;
    padding: 0;
    color: var(--white);
    font-size: 12px;
    line-height: 19px;
    text-align: right;
    white-space: nowrap;
  }
  .contact__line {
    display: flex;
    justify-content: flex-end;
    align-items: center;
    gap: 6px;
  }
  .contact__icon {
    width: 11px;
    height: 11px;
    flex: none;
  }
</style>
</head>
<body>
<main class="sheet">

  <section class="card card--back" aria-label="Card back">
    <div class="brand">
      <span class="brand__mark"></span>
      <span class="brand__name">Tramvexa</span>
    </div>
  </section>

  <section class="card card--front" aria-label="Card front">
    <svg class="swoosh" viewBox="0 0 660 377" aria-hidden="true">
      <path d="M660,6 C560,14 466,44 404,104 C334,174 250,304 132,377" fill="none" stroke="var(--red)" stroke-width="10"/>
      <path d="M660,22 C560,30 470,60 410,120 C340,190 260,320 150,377 L660,377 Z" fill="var(--navy)"/>
      <path d="M0,326 C100,352 200,352 290,324 C220,360 110,370 0,348 Z" fill="var(--red)"/>
    </svg>

    <div class="brand">
      <span class="brand__mark"></span>
      <span class="brand__name">Tramvexa</span>
    </div>

    <div class="holder">
      <p class="holder__name">Delia Marsh-Corbin</p>
      <p class="holder__role">Consultant</p>
    </div>

    <ul class="contact">
      <li class="contact__line">914 E Harlan Avenue, Suite 215</li>
      <li class="contact__line">Fort Worth, TX 76102</li>
      <li class="contact__line">817 555 0142
        <svg class="contact__icon" viewBox="0 0 12 12" aria-hidden="true"><path d="M2,1 L4.5,1 L5.5,3.8 L4,4.8 C4.8,6.4 5.6,7.2 7.2,8 L8.2,6.5 L11,7.5 L11,10 C6,10.5 1.5,6 2,1 Z" fill="var(--white)"/></svg>
      </li>
      <li class="contact__line">rdunmore@tramvexa-mail.com
        <svg class="contact__icon" viewBox="0 0 12 12" aria-hidden="true"><rect x="1" y="2.5" width="10" height="7" fill="var(--white)"/><path d="M1,2.5 L6,6.5 L11,2.5" fill="none" stroke="var(--navy)" stroke-width="1"/></svg>
      </li>
      <li class="contact__line">www.tramvexa-site.com</li>
    </ul>
  </section>

</main>
</body>
</html>
```